Flyer-Design für Vermittlung von Immobilien
Zielgruppe
Immobilien vermitteln, für Käufer und Verkäufer, für Mieter und Vermieter
Aufgabenstellung
Inhalt Seite 1: Wir verkaufen Ihr Grundstück, Ihr Haus, Ihre Wohnung
Inhalt Seite 2: Wir suchen für solvente Kunden Ihr Grundstück, Ihr Haus, Ihre Wohnung
Weiterhin soll das Design in Anlehnung der DOLKAN Visitenkarte (siehe vorhergehendes Projekt) layoutet werden. Die Kontakte sollen explizit auf einen Makler mit Foto verweisen.

```html
<!DOCTYPE html>
<html lang="de">
<head>
<meta charset="utf-8">
<title>DOLKAN Immobilien – Flyer</title>
<link rel="stylesheet" href="https://fonts.googleapis.com/css2?family=Rubik:wght@400;500;700&display=swap">
<style>
  :root {
    --navy: #13253f;
    --navy-light: #2c3c5c;
    --ink: #13233c;
    --white: #ffffff;
    --paper: #ffffff;
    --text-soft: #e6e9ef;
  }
  * { box-sizing: border-box; margin: 0; padding: 0; }
  html, body { width: 1200px; height: 1118px; overflow: hidden; background: var(--paper); }
  body { position: relative; font-family: "Rubik", Arial, sans-serif; color: var(--ink); }

  .flyer-page {
    position: absolute; width: 501px; height: 999px; overflow: hidden;
    background: linear-gradient(105deg, var(--navy-light) 0%, var(--navy) 45%, var(--navy) 100%);
    box-shadow: 0 4px 22px rgba(0,0,0,0.18);
  }
  .flyer-page--front { left: 65px; top: 66px; }
  .flyer-page--back { left: 646px; top: 64px; }

  .hero-photo { position: absolute; left: 0; top: 0; width: 100%; }
  .hero-photo--residence {
    height: 698px;
    background: linear-gradient(160deg, #7fb6e6 0%, #c9d3d8 30%, #dcd8cc 48%, #8eae5a 72%, #b9c79a 100%);
  }
  .hero-photo--handshake {
    height: 333px;
    background: linear-gradient(120deg, #4d4540 0%, #8a7868 40%, #c9b7a2 60%, #5c6470 100%);
  }

  .speech-bubble {
    position: absolute; left: 45px; width: 406px; background: var(--white);
    text-align: center; color: var(--ink);
  }
  .speech-bubble__tail { position: absolute; }
  .speech-bubble__title { font-weight: 700; font-size: 37px; line-height: 46px; }
  .speech-bubble__sub { font-weight: 700; font-size: 24px; line-height: 35px; }

  .bubble-search { top: 39px; height: 200px; padding-top: 14px; }
  .bubble-search .speech-bubble__sub { margin-top: 6px; }
  .bubble-sell { top: 433px; height: 167px; padding-top: 20px; }
  .bubble-sell .speech-bubble__sub { margin-top: 6px; }
  .bubble-team { top: 39px; height: 128px; padding-top: 14px; }
  .bubble-team .speech-bubble__title { font-size: 37px; line-height: 48px; }
  .bubble-team .speech-bubble__sub { margin-top: 10px; }

  .call-to-action {
    position: absolute; top: 737px; left: 0; width: 100%; text-align: center; color: var(--white);
  }
  .call-to-action__head { font-weight: 700; font-size: 24px; line-height: 30px; }
  .call-to-action__line { font-weight: 400; font-size: 24px; line-height: 36px; }

  .brand {
    position: absolute; left: 0; width: 100%; text-align: center; color: var(--white);
  }
  .brand__square {
    display: block; margin: 0 auto 18px; width: 34px; height: 34px;
    border: 3px solid var(--white);
  }
  .brand__name {
    font-weight: 500; font-size: 26px; letter-spacing: 12px; padding-left: 12px;
  }
  .flyer-page--front .brand { top: 862px; }
  .flyer-page--back .brand { top: 792px; }

  .agent { position: absolute; left: 61px; width: 420px; height: 152px; }
  .agent--first { top: 367px; }
  .agent--second { top: 557px; }
  .agent__photo {
    position: absolute; left: 0; top: 0; width: 114px; height: 152px;
    background: linear-gradient(180deg, #b9b6b1 0%, #9c948c 55%, #3a3d45 100%);
  }
  .agent__info { position: absolute; left: 138px; top: 17px; color: var(--text-soft); font-size: 13px; line-height: 17px; }
  .agent__name { font-weight: 700; color: var(--white); }
  .agent__role { margin-bottom: 16px; }
  .agent__contacts { display: grid; grid-template-columns: 76px auto; row-gap: 0; }

  .company-contact {
    position: absolute; top: 906px; left: 0; width: 100%; text-align: center;
    color: var(--text-soft); font-size: 13.5px; line-height: 17px;
  }
  .company-contact__web { font-weight: 700; color: var(--white); }
</style>
</head>
<body>

<section class="flyer-page flyer-page--front">
  <div class="hero-photo hero-photo--residence" role="img" aria-label="Foto: moderne Wohnanlage mit Bäumen, Gehweg und blühenden Gräsern"></div>

  <div class="speech-bubble bubble-search">
    <p class="speech-bubble__title">Wir suchen für<br>solvente Kunden</p>
    <p class="speech-bubble__sub">Ihr Grundstück, Ihr Haus,<br>Ihre Wohnung!</p>
    <svg class="speech-bubble__tail" style="left:36px;top:199px" width="56" height="46" viewBox="0 0 56 46"><polygon points="0,0 56,0 56,46" fill="#fff"/></svg>
  </div>

  <div class="speech-bubble bubble-sell">
    <p class="speech-bubble__title">Wir verkaufen</p>
    <p class="speech-bubble__sub">Ihr Grundstück, Ihr Haus,<br>Ihre Wohnung!</p>
    <svg class="speech-bubble__tail" style="left:315px;top:166px" width="56" height="48" viewBox="0 0 56 48"><polygon points="0,48 0,0 56,0" fill="#fff"/></svg>
  </div>

  <div class="call-to-action">
    <p class="call-to-action__head">Rufen Sie uns an!</p>
    <p class="call-to-action__line">Wir beraten Sie gerne.</p>
  </div>

  <div class="brand">
    <span class="brand__square"></span>
    <p class="brand__name">DOLKAN</p>
  </div>
</section>

<section class="flyer-page flyer-page--back">
  <div class="hero-photo hero-photo--handshake" role="img" aria-label="Foto: Handschlag zweier Geschäftsleute am Tisch mit Kaffeetasse"></div>

  <div class="speech-bubble bubble-team">
    <p class="speech-bubble__title">Unser Team</p>
    <p class="speech-bubble__sub">arbeitet für Ihren Erfolg!</p>
    <svg class="speech-bubble__tail" style="left:315px;top:127px" width="56" height="48" viewBox="0 0 56 48"><polygon points="0,48 0,0 56,0" fill="#fff"/></svg>
  </div>

  <article class="agent agent--first">
    <div class="agent__photo" role="img" aria-label="Porträtfoto des Geschäftsführers"></div>
    <div class="agent__info">
      <p class="agent__name">Lukas Berger</p>
      <p class="agent__role">Betriebswirt / Geschäftsführer</p>
      <div class="agent__contacts">
        <span>Mobil:</span><span>+49 (0) 170 12 345 678</span>
        <span>Fax:</span><span>+49 (0) 30 98 765 43 21</span>
        <span>WhatsApp:</span><span>+49 (0) 170 12 345 678</span>
        <span>E-Mail:</span><span>l.berger@dolkan.immo</span>
      </div>
    </div>
  </article>

  <article class="agent agent--second">
    <div class="agent__photo" role="img" aria-label="Porträtfoto der Immobilienberaterin"></div>
    <div class="agent__info">
      <p class="agent__name">Anna Weber</p>
      <p class="agent__role">Meister(in) / Immobilienberatung</p>
      <div class="agent__contacts">
        <span>Mobil:</span><span>+49 (0) 171 2 46 80 13</span>
        <span>Fax:</span><span>+49 (0) 30 98 765 43 21</span>
        <span>WhatsApp:</span><span>+49 (0) 171 2 46 80 13</span>
        <span>E-Mail:</span><span>a.weber@dolkan.immo</span>
      </div>
    </div>
  </article>

  <div class="brand">
    <span class="brand__square"></span>
    <p class="brand__name">DOLKAN</p>
  </div>

  <div class="company-contact">
    <p>Lindenallee 12 &nbsp;I&nbsp; 04109 Leipzig</p>
    <p>+49 (0) 170 12 345 678 &nbsp;I&nbsp; l.berger@dolkan.immo</p>
    <p class="company-contact__web">www.dolkan.immo</p>
  </div>
</section>

</body>
</html>
```